Vexmora Stationary
Project: Vexmora Stationary
Vexmora Stationary - Information Technology
Creative Brief
Modern
Mathieu Ferrand
Associate
Av. Pierre Dumel 42 CH-1209 Geneva
mferrand@vexmora.com
www.vexmora.com

```html
<!DOCTYPE html>
<html lang="en">
<head>
<meta charset="utf-8">
<title>Vexmora Stationary</title>
<link href="https://fonts.googleapis.com/css2?family=Open+Sans:wght@400;700&display=swap" rel="stylesheet">
<style>
  :root{
    --bg:#5b5d60;
    --paper:#ffffff;
    --blue:#1e8fe1;
    --blue-deep:#0f6fbf;
    --ink:#2a2c30;
    --muted:#8a8f96;
    --line:#d5d9de;
  }
  *{box-sizing:border-box;margin:0;padding:0}
  html,body{width:1200px;height:221px;overflow:hidden;background:var(--bg);font-family:"Open Sans",Arial,sans-serif;color:var(--ink)}
  .sheet{position:absolute;background:var(--paper);box-shadow:0 1px 3px rgba(0,0,0,.25)}
  .sheet.is-blue{background:linear-gradient(135deg,var(--blue),var(--blue-deep));color:#fff}
  .brand{display:flex;align-items:center;gap:3px;font-weight:700;color:var(--blue);line-height:1}
  .brand .mark{display:inline-block;background:var(--blue)}
  .is-blue .brand{color:#fff}
  .is-blue .brand .mark{background:#fff}
  .small-text{font-size:4px;line-height:1.5;color:var(--muted)}
  .body-text{font-size:4.5px;line-height:1.6;color:var(--muted)}
  .footer-band{position:absolute;left:0;right:0;bottom:0;height:6px;background:var(--blue)}

  /* business cards */
  .card-front{left:14px;top:30px;width:110px;height:62px;padding:8px}
  .card-front .brand{font-size:11px}
  .card-front .brand .mark{width:8px;height:8px}
  .card-front .person{margin-top:10px;font-size:5px;font-weight:700;color:var(--ink)}
  .card-front .role{font-size:4px;color:var(--blue)}
  .card-back{left:14px;top:100px;width:110px;height:62px;display:flex;align-items:center;justify-content:center}
  .card-back .brand{font-size:13px}
  .card-back .brand .mark{width:9px;height:9px}

  /* letterheads */
  .letterhead{top:14px;width:112px;height:158px;padding:10px 9px}
  .letterhead.first{left:146px}
  .letterhead.second{left:268px}
  .letterhead .brand{font-size:10px}
  .letterhead .brand .mark{width:7px;height:7px}
  .letterhead .address{margin-top:12px}
  .letterhead .body-text{margin-top:14px}
  .letterhead .sign{margin-top:14px;font-size:4.5px;font-weight:700;color:var(--ink)}

  /* compliment slip */
  .slip{left:394px;top:24px;width:140px;height:70px;padding:10px}
  .slip .brand{font-size:12px}
  .slip .brand .mark{width:8px;height:8px}
  .slip .note{margin-top:16px;font-size:6px;color:var(--blue)}

  .envelope-c5{left:394px;top:104px;width:140px;height:90px;padding:10px}
  .envelope-c5 .brand{font-size:10px}
  .envelope-c5 .brand .mark{width:7px;height:7px}

  /* DL envelopes */
  .envelope-dl{left:552px;width:176px;height:62px;padding:9px}
  .envelope-dl.front{top:30px}
  .envelope-dl.back{top:104px;display:flex;align-items:center;justify-content:center}
  .envelope-dl .brand{font-size:10px}
  .envelope-dl .brand .mark{width:7px;height:7px}
  .envelope-dl.back .brand{font-size:14px}
  .envelope-dl.back .brand .mark{width:10px;height:10px}

  /* folder */
  .folder-inside{left:748px;top:20px;width:150px;height:184px;padding:12px}
  .folder-inside .pocket{position:absolute;left:0;right:0;bottom:0;height:62px;background:var(--blue);clip-path:polygon(0 22%,100% 0,100% 100%,0 100%)}
  .folder-inside .card-slot{position:absolute;right:16px;bottom:20px;width:44px;height:26px;border:1px solid rgba(255,255,255,.7)}
  .folder-cover{left:902px;top:20px;width:150px;height:184px;display:flex;align-items:center;justify-content:center}
  .folder-cover .brand{font-size:16px}
  .folder-cover .brand .mark{width:11px;height:11px}

  /* disc */
  .disc{position:absolute;left:1068px;top:40px}
  .disc .brand-label{font:700 9px "Open Sans",Arial,sans-serif;fill:#fff}
</style>
</head>
<body>

  <section class="sheet card-front" aria-label="Business card front">
    <div class="brand"><span class="mark"></span>vexmora</div>
    <p class="person">Mathieu Ferrand</p>
    <p class="role">Associate</p>
    <p class="small-text">Av. Pierre Dumel 42 CH-1209 Geneva<br>mferrand@vexmora.com · www.vexmora.com</p>
  </section>

  <section class="sheet is-blue card-back" aria-label="Business card back">
    <div class="brand"><span class="mark"></span>vexmora</div>
  </section>

  <section class="sheet letterhead first" aria-label="Letterhead">
    <div class="brand"><span class="mark"></span>vexmora</div>
    <p class="small-text address">Av. Pierre Dumel 42 CH-1209 Geneva<br>www.vexmora.com</p>
    <p class="body-text">Dear client, thank you for your trust.</p>
    <p class="sign">Mathieu Ferrand</p>
    <div class="footer-band"></div>
  </section>

  <section class="sheet letterhead second" aria-label="Letterhead second page">
    <div class="brand"><span class="mark"></span>vexmora</div>
    <p class="small-text address">mferrand@vexmora.com<br>vexmora.com</p>
    <p class="body-text">We look forward to working together.</p>
    <div class="footer-band"></div>
  </section>

  <section class="sheet slip" aria-label="Compliment slip">
    <div class="brand"><span class="mark"></span>vexmora</div>
    <p class="note">With compliments</p>
  </section>

  <section class="sheet envelope-c5" aria-label="Large envelope">
    <div class="brand"><span class="mark"></span>vexmora</div>
    <p class="small-text">Av. Pierre Dumel 42 CH-1209 Geneva</p>
    <div class="footer-band"></div>
  </section>

  <section class="sheet envelope-dl front" aria-label="DL envelope front">
    <div class="brand"><span class="mark"></span>vexmora</div>
    <p class="small-text">Av. Pierre Dumel 42 CH-1209 Geneva</p>
    <div class="footer-band"></div>
  </section>

  <section class="sheet is-blue envelope-dl back" aria-label="DL envelope back">
    <div class="brand"><span class="mark"></span>vexmora</div>
  </section>

  <section class="sheet folder-inside" aria-label="Presentation folder inside">
    <div class="brand" style="font-size:10px"><span class="mark" style="width:7px;height:7px"></span>vexmora</div>
    <div class="pocket"></div>
    <div class="card-slot"></div>
  </section>

  <section class="sheet is-blue folder-cover" aria-label="Presentation folder cover">
    <div class="brand"><span class="mark"></span>vexmora</div>
  </section>

  <svg class="disc" width="120" height="120" viewBox="0 0 120 120" aria-label="Disc label">
    <defs>
      <linearGradient id="discFill" x1="0" y1="0" x2="1" y2="1">
        <stop offset="0" stop-color="#1e8fe1"/>
        <stop offset="1" stop-color="#0f6fbf"/>
      </linearGradient>
    </defs>
    <circle cx="60" cy="60" r="56" fill="url(#discFill)"/>
    <circle cx="60" cy="60" r="14" fill="#e8ebee"/>
    <circle cx="60" cy="60" r="6" fill="#5b5d60"/>
    <text class="brand-label" x="60" y="92" text-anchor="middle">vexmora</text>
  </svg>

</body>
</html>
```